Bright Harbor Realty

We need a good looking flyer for our real estate company to impress people who are considering to sell their homes for as low as 1.5% listing commission. Please see flyer examples for reference.
555-318-4906

```html
<!DOCTYPE html>
<html lang="en">
<head>
<meta charset="utf-8">
<title>Just Sold Flyer – Bright Harbor Realty</title>
<link href="https://fonts.googleapis.com/css2?family=Montserrat:wght@500;600;700;800&family=Open+Sans:wght@400;600;700&family=Baloo+2:wght@700;800&display=swap" rel="stylesheet">
<style>
  :root{
    --blue:#1f5fb4;
    --blue-dark:#124a98;
    --blue-light:#3b86d6;
    --red:#e32b2b;
    --ink:#1a1a1a;
    --grey-text:#5a5a5a;
    --grey-band:#d9d9d9;
    --page-bg:#e9e9e9;
    --white:#ffffff;
    --navy:#1b2f6b;
  }
  *{box-sizing:border-box;margin:0;padding:0}
  html,body{width:707px;height:1200px;overflow:hidden;background:var(--page-bg)}
  body{position:relative;font-family:"Open Sans",Arial,sans-serif}
  .flyer{position:absolute;left:14px;top:119px;width:680px;height:962px;background:var(--white);overflow:hidden;box-shadow:0 3px 10px rgba(0,0,0,.18)}
  .abs{position:absolute}

  /* header */
  .header{left:0;top:0;width:680px;height:130px;background:linear-gradient(180deg,var(--blue-light) 0%,var(--blue) 55%,var(--blue-dark) 100%)}
  .header-frame{left:8px;top:8px;right:8px;bottom:8px;border:1.5px solid rgba(255,255,255,.85)}
  .headline{left:0;top:12px;width:100%;text-align:center;font-family:"Montserrat",Arial,sans-serif;font-weight:800;font-size:72px;color:var(--white);letter-spacing:1px;line-height:1}
  .subline{left:0;top:90px;width:100%;text-align:center;font-family:"Open Sans",Arial,sans-serif;font-weight:600;font-size:18px;color:var(--white)}

  /* hero */
  .hero-photo{left:0;top:130px;width:463px;height:378px;background:linear-gradient(135deg,#cfd3d8 0%,#e8e8e6 40%,#b9c3cf 75%,#8f9aa6 100%)}
  .hero-frame{left:12px;top:146px;width:439px;height:350px;border:1.5px solid rgba(255,255,255,.9)}
  .brand{left:463px;top:130px;width:217px;height:138px;display:flex;align-items:center;justify-content:center;gap:8px}
  .brand-mark{width:14px;height:14px;background:var(--navy)}
  .brand-name{font-family:"Open Sans",Arial,sans-serif;font-weight:700;font-size:17px;color:var(--navy)}
  .side-photo{left:469px;top:268px;width:205px;height:236px;background:linear-gradient(180deg,#7fb1e3 0%,#c9dcee 35%,#a79584 65%,#5d7048 100%)}

  /* listings */
  .listings-band{left:0;top:508px;width:680px;height:220px;background:var(--grey-band)}
  .listings-blue{left:0;top:646px;width:680px;height:82px;background:linear-gradient(180deg,var(--blue) 0%,var(--blue-dark) 100%)}
  .listing{top:525px;width:206px;height:155px}
  .listing-photo{width:100%;height:100%;border:2px solid var(--white)}
  .listing-1 .listing-photo{background:linear-gradient(180deg,#8cbde8 0%,#c7dbe9 40%,#7aa45a 70%,#58803c 100%)}
  .listing-2 .listing-photo{background:linear-gradient(180deg,#9cc6ea 0%,#dedad0 45%,#c9c4b6 70%,#6f9450 100%)}
  .listing-3 .listing-photo{background:linear-gradient(180deg,#6d9b4e 0%,#c8cf9e 45%,#b7b48d 70%,#5f8a3f 100%)}
  .save-tag{position:absolute;right:2px;bottom:14px;background:var(--red);color:var(--white);font-family:"Montserrat",Arial,sans-serif;font-weight:700;font-size:11.5px;padding:3px 8px 3px 16px;clip-path:polygon(10px 0,100% 0,100% 100%,10px 100%,0 50%)}
  .listing-address{top:684px;width:220px;text-align:center;color:var(--white);font-size:11px;line-height:1.35}
  .listing-address strong{font-weight:700}

  /* agent */
  .agent-photo{left:12px;top:738px;width:213px;height:212px;background:linear-gradient(180deg,#dcdcdc 0%,#c9c9c9 50%,#3a3f48 100%)}
  .agent-name{left:12px;top:922px;width:210px;height:28px;background:var(--red);color:var(--white);font-family:"Montserrat",Arial,sans-serif;font-weight:700;font-size:17px;display:flex;align-items:center;justify-content:center;letter-spacing:.5px}

  /* pitch */
  .pitch-title{left:235px;top:734px;width:445px;text-align:center;font-family:"Baloo 2",Arial,sans-serif;font-weight:800;font-size:54px;line-height:1;color:var(--blue)}
  .pitch-body{left:240px;top:788px;width:432px;text-align:center;font-size:15.5px;line-height:1.3;color:var(--grey-text)}
  .cta-bar{left:233px;top:860px;width:438px;height:29px;background:var(--ink);color:var(--white);font-family:"Montserrat",Arial,sans-serif;font-weight:700;font-size:20px;display:flex;align-items:center;justify-content:center}
  .phone-bar{left:233px;top:891px;width:438px;height:59px;background:linear-gradient(180deg,var(--blue-light) 0%,var(--blue) 60%,var(--blue-dark) 100%);display:flex;align-items:center;justify-content:center;gap:22px}
  .phone-icon{width:32px;height:32px}
  .phone-number{font-family:"Montserrat",Arial,sans-serif;font-weight:800;font-size:44px;color:var(--white);letter-spacing:1px}
</style>
</head>
<body>
<main class="flyer">
  <header>
    <div class="abs header"></div>
    <div class="abs header-frame"></div>
    <h1 class="abs headline">JUST SOLD</h1>
    <p class="abs subline">List For 1.5% Commission, Still Receive Top Marketing!</p>
  </header>

  <section class="hero">
    <div class="abs hero-photo" role="img" aria-label="Photo of a bright living room with sofa, rug and large windows"></div>
    <div class="abs hero-frame"></div>
    <div class="abs brand"><span class="brand-mark"></span><span class="brand-name">Bright Harbor Realty</span></div>
    <div class="abs side-photo" role="img" aria-label="Photo of a two-storey house exterior with trees and blue sky"></div>
  </section>

  <section class="listings">
    <div class="abs listings-band"></div>
    <div class="abs listings-blue"></div>

    <div class="abs listing listing-1" style="left:10px">
      <div class="listing-photo" role="img" aria-label="Photo of a single-storey home with lawn"></div>
      <span class="save-tag">SAVE $3,750</span>
    </div>
    <p class="abs listing-address" style="left:3px">2418 Maple Crest Circle Fairhaven,<br>Fl 33400 - <strong>$250,00</strong></p>

    <div class="abs listing listing-2" style="left:237px">
      <div class="listing-photo" role="img" aria-label="Photo of a two-storey home with garage"></div>
      <span class="save-tag">SAVE $4,200</span>
    </div>
    <p class="abs listing-address" style="left:230px">7520 E Harbor Ridge Drive Oakmont,<br>Fl 33402 - <strong>$280,000</strong></p>

    <div class="abs listing listing-3" style="left:464px">
      <div class="listing-photo" role="img" aria-label="Photo of a small home with garage and trees"></div>
      <span class="save-tag">SAVE $3,350</span>
    </div>
    <p class="abs listing-address" style="left:457px">4096 Willow Bend Circle Fairhaven,<br>Fl 33400 - <strong>$335,000</strong></p>
  </section>

  <section class="agent">
    <div class="abs agent-photo" role="img" aria-label="Portrait photo of the listing agent in a suit"></div>
    <div class="abs agent-name">MARCUS DELANE</div>
  </section>

  <section class="pitch">
    <h2 class="abs pitch-title">Did You Know?</h2>
    <p class="abs pitch-body">On average, Our customers save $ 8,750 when they choose us...and they still receive top marketing, service and representation!</p>
    <div class="abs cta-bar">Call us today and save Thousands!</div>
    <div class="abs phone-bar">
      <svg class="phone-icon" viewBox="0 0 32 32" aria-hidden="true">
        <path d="M9 4c1 0 2 2 3 4s0 3-1 4c1 3 4 6 7 7 1-1 2-2 4-1s4 2 4 3-2 5-5 5C12 26 6 20 6 10c0-3 2-6 3-6z" fill="none" stroke="#fff" stroke-width="2.4" stroke-linejoin="round"/>
        <path d="M19 8a6 6 0 0 1 5 5M19 3a11 11 0 0 1 10 10" fill="none" stroke="#fff" stroke-width="2.2" stroke-linecap="round"/>
      </svg>
      <span class="phone-number">555-318-4906</span>
    </div>
  </section>
</main>
</body>
</html>
```